Bref créative
Blue Maple Holdings, LLC
Business cards, stationary and envelopes, electronic stationary (Microsoft Word), email signature
Simple
Peter L. Ward
Managing Member
5180 Halvern Court, Suite A
Columbia, MO 65203
pward@bmholdco.example
Phone, email, and name will change for the additional members of the company.
We also want an electronic email signature, and electronic stationary to be used with Microsoft word.
Stationary and envelopes should tie in the theme of the business cards for a uniform look.
Also looking for a Header only version of the stationary, as well as a full page version (header and footer used for design).
Logo used in a creative way.
Horizontal Black Background
Horizontal ALL Black
Horizontal White Background
Horizontal ALL White
Vertical Black Background
Vertical ALL Black
Vertical White Background
Vertical ALL White

```html
<!DOCTYPE html>
<html lang="en">
<head>
<meta charset="utf-8">
<title>Blue Maple Holdings — Business Cards</title>
<link href="https://fonts.googleapis.com/css2?family=Michroma&family=Open+Sans:ital,wght@0,400;0,600;0,700;1,400&display=swap" rel="stylesheet">
<style>
  :root{
    --board:#8f8f8f;
    --board-dark:#7c7c7c;
    --card-white:#ffffff;
    --card-black:#1e1e1e;
    --brand-red:#c8302e;
    --band-light:#de5a52;
    --band-dark:#ad221f;
    --rule:#a3a3a3;
    --label:#f4f4f4;
    --ink-white:#ffffff;
  }
  *{margin:0;padding:0;box-sizing:border-box}
  html,body{width:1200px;height:806px;overflow:hidden}
  body{
    background:radial-gradient(ellipse at center,var(--board) 0%,var(--board-dark) 100%);
    font-family:"Open Sans",Arial,sans-serif;
    position:relative;
  }

  .card{
    position:absolute;width:497px;height:283px;border-radius:14px;overflow:hidden;
    box-shadow:0 2px 6px rgba(0,0,0,.25);
  }
  .card--white{background:var(--card-white)}
  .card--black{background:var(--card-black)}
  .front-a{left:72px;top:43px}
  .front-b{left:638px;top:43px}
  .back-a{left:72px;top:422px}
  .back-b{left:638px;top:422px}

  .card-label{
    position:absolute;width:497px;text-align:center;
    font-family:"Michroma",sans-serif;font-size:15px;letter-spacing:1.5px;line-height:20px;
    color:var(--label);
  }
  .label-front-a{left:72px;top:352px}
  .label-front-b{left:638px;top:352px}
  .label-back-a{left:72px;top:739px}
  .label-back-b{left:638px;top:739px}

  .brand-name{
    display:flex;align-items:center;gap:10px;
    font-family:"Open Sans",sans-serif;font-weight:700;color:var(--brand-red);
    text-transform:uppercase;letter-spacing:.5px;white-space:nowrap;
  }
  .brand-mark{flex:none;background:var(--brand-red)}
  .front .brand-name{position:absolute;left:30px;top:48px;font-size:24px;line-height:38px}
  .front .brand-mark{width:34px;height:34px}

  .band{
    position:absolute;left:0;right:0;top:140px;bottom:0;
    background:radial-gradient(ellipse at 55% 25%,var(--band-light) 0%,var(--brand-red) 45%,var(--band-dark) 100%);
    border-top:3px solid var(--rule);
  }
  .contact{position:absolute;left:26px;top:18px;list-style:none;color:var(--ink-white);font-size:10.5px;line-height:16px}
  .contact li{display:flex;align-items:center;gap:9px}
  .contact .address{line-height:12px;font-style:italic;margin-bottom:6px}
  .contact svg{width:9px;height:9px;flex:none;fill:var(--ink-white)}
  .person{position:absolute;right:20px;bottom:18px;color:var(--ink-white);font-size:12.5px;line-height:16px}
  .person strong{font-weight:700}

  .back .brand-name{
    position:absolute;left:0;right:0;top:134px;justify-content:center;font-size:26px;line-height:38px;
  }
  .back .brand-mark{width:34px;height:34px}
</style>
</head>
<body>

<section class="card card--white front front-a">
  <div class="brand-name"><span class="brand-mark"></span>Blue Maple Holdings</div>
  <div class="band">
    <ul class="contact">
      <li class="address"><svg viewBox="0 0 12 12"><path d="M6 0C3.8 0 2 1.8 2 4c0 3 4 8 4 8s4-5 4-8c0-2.2-1.8-4-4-4zm0 5.5A1.5 1.5 0 1 1 6 2.5a1.5 1.5 0 0 1 0 3z"/></svg><span>5180 Halvern Court, Suite A<br>Columbia, MO 65203</span></li>
      <li><svg viewBox="0 0 12 12"><path d="M2.5 0l2 2.5-1.2 1.5c.8 1.8 2.1 3.1 3.9 3.9L8.7 6.7l2.8 2-1 2.8C5.2 11.5.5 6.8.5 1.5z"/></svg>(573) 555-0142</li>
      <li><svg viewBox="0 0 12 12"><rect x="3" y="0" width="6" height="12" rx="1"/></svg>(573) 555-0143</li>
      <li><svg viewBox="0 0 12 12"><path d="M1 4h10v6H1zM3 0h6v3H3z"/></svg>(573) 555-0178</li>
      <li><svg viewBox="0 0 12 12"><path d="M0 2h12v8H0z"/></svg>pward@bmholdco.example</li>
    </ul>
    <p class="person"><strong>Peter L. Ward</strong> | <span class="title">Managing Member</span></p>
  </div>
</section>

<section class="card card--black front front-b">
  <div class="brand-name"><span class="brand-mark"></span>Blue Maple Holdings</div>
  <div class="band">
    <ul class="contact">
      <li class="address"><svg viewBox="0 0 12 12"><path d="M6 0C3.8 0 2 1.8 2 4c0 3 4 8 4 8s4-5 4-8c0-2.2-1.8-4-4-4zm0 5.5A1.5 1.5 0 1 1 6 2.5a1.5 1.5 0 0 1 0 3z"/></svg><span>5180 Halvern Court, Suite A<br>Columbia, MO 65203</span></li>
      <li><svg viewBox="0 0 12 12"><path d="M2.5 0l2 2.5-1.2 1.5c.8 1.8 2.1 3.1 3.9 3.9L8.7 6.7l2.8 2-1 2.8C5.2 11.5.5 6.8.5 1.5z"/></svg>(573) 555-0142</li>
      <li><svg viewBox="0 0 12 12"><rect x="3" y="0" width="6" height="12" rx="1"/></svg>(573) 555-0143</li>
      <li><svg viewBox="0 0 12 12"><path d="M1 4h10v6H1zM3 0h6v3H3z"/></svg>(573) 555-0178</li>
      <li><svg viewBox="0 0 12 12"><path d="M0 2h12v8H0z"/></svg>pward@bmholdco.example</li>
    </ul>
    <p class="person"><strong>Peter L. Ward</strong> | <span class="title">Managing Member</span></p>
  </div>
</section>

<p class="card-label label-front-a">Business Card Front A</p>
<p class="card-label label-front-b">Business Card Front B</p>

<section class="card card--white back back-a">
  <div class="brand-name"><span class="brand-mark"></span>Blue Maple Holdings</div>
</section>

<section class="card card--black back back-b">
  <div class="brand-name"><span class="brand-mark"></span>Blue Maple Holdings</div>
</section>

<p class="card-label label-back-a">Business Card Back A</p>
<p class="card-label label-back-b">Business Card Back B</p>

</body>
</html>
```